Quarry - Web Design Project

We are seeking to have our website redesigned. Our current webpage is rather dated looking www.quarry-results.com We will be utilizing similar content to explain our services as what is in the website now. We do not see it at a retail portal but rather a website for those inquiring about our services as a reference check so to speak.

We wish to have a look that is considered clean, fresh, contemporary and contains a business savvy vibe.

We prefer isolated white background and also wish to retain the integrity of our Logo and colour scheme.

We are looking for something that doesnt look like it was designed at home on sitemarlo. We are hoping to find something that looks like it would reside on a tablet.

Hello designers!

We apologize for our tardiness as we have been quite preoccupied. We will be extending our invites to the end of January!

Hello All,

Please review our offer once again for updated requirements.  We are hoping to accept a design by months end.

Quarry

Target Market(s)

Business to business clients and Large manufacturers

Industry/Entity Type

Retail

Requirements
Must have
• Existing Logo

There must be an area dedicated to an intro video that will be incorporated on our landing page.

We require design of the other pages as well not only the landing page.

```html
<!DOCTYPE html>
<html lang="en">
<head>
<meta charset="utf-8">
<title>Quarry Performance Group</title>
<link rel="stylesheet" href="https://fonts.googleapis.com/css2?family=Carlito:wght@400;700&family=Open+Sans:wght@600;700&family=Arimo&display=swap">
<style>
  :root {
    --page-bg: #ececec;
    --white: #ffffff;
    --black: #000000;
    --red: #e3201f;
    --red-soft: #ec4a4f;
    --panel: #eeeeee;
    --panel-line: #dddddd;
    --text: #111111;
    --logo-grey: #55504f;
    --social: #4a90d0;
    --sky-top: #1f2f8f;
    --sky-mid: #3b5cc4;
    --sea: #2c6fd0;
  }
  * { margin: 0; padding: 0; box-sizing: border-box; }
  html, body { width: 1200px; height: 877px; overflow: hidden; }
  body { background: var(--page-bg); font-family: "Carlito", sans-serif; color: var(--text); position: relative; }

  .site { position: absolute; left: 144px; top: 13px; width: 912px; height: 855px; background: var(--white); box-shadow: 0 0 6px rgba(0,0,0,.45); border-radius: 6px; }

  .utility-bar { position: absolute; left: 592px; top: 0; width: 285px; height: 31px; background: var(--black); border-radius: 0 0 5px 5px; display: flex; align-items: center; padding: 0 4px 0 9px; gap: 5px; font-family: "Open Sans", sans-serif; font-weight: 700; font-size: 12.5px; color: var(--white); white-space: nowrap; }
  .utility-bar .divider { font-weight: 600; }
  .utility-bar .follow { color: var(--red); text-decoration: underline; font-size: 11.5px; margin-left: 2px; }
  .social-square { flex: 0 0 auto; width: 23px; height: 22px; background: var(--social); border-radius: 3px; margin-left: 3px; }

  .brand { position: absolute; left: 24px; top: 48px; display: flex; align-items: center; gap: 8px; font-family: "Carlito", sans-serif; font-weight: 700; font-size: 46px; color: var(--logo-grey); }
  .brand-dot { width: 14px; height: 14px; border-radius: 50%; background: var(--red); }

  .search { position: absolute; left: 686px; top: 70px; display: flex; gap: 5px; }
  .search-field { width: 156px; height: 21px; border: 1px solid #dcdcdc; font-family: "Arimo", sans-serif; font-size: 12px; display: flex; align-items: center; gap: 8px; padding-left: 6px; color: #222; }
  .search-go { width: 29px; height: 21px; background: var(--black); color: var(--white); font-family: "Open Sans", sans-serif; font-size: 9px; font-weight: 700; display: flex; align-items: center; justify-content: center; }

  .main-nav { position: absolute; left: 0; top: 128px; width: 912px; height: 45px; background: var(--black); border-bottom: 3px solid var(--red); }
  .main-nav a { position: absolute; top: 0; height: 42px; line-height: 42px; font-family: "Open Sans", sans-serif; font-weight: 700; font-size: 11.8px; color: var(--white); text-decoration: none; white-space: nowrap; }
  .main-nav a.active { background: var(--red); width: 71px; text-align: center; }

  .hero { position: absolute; left: 25px; top: 175px; width: 862px; height: 305px; border: 3px solid var(--red); border-top: 0; border-radius: 0 0 6px 6px; overflow: hidden;
    background: linear-gradient(180deg, var(--sky-top) 0%, var(--sky-mid) 45%, #c9d6ee 62%, var(--sea) 72%, #5d7fb8 100%); }
  .hero-caption { position: absolute; left: 0; bottom: 0; width: 100%; padding: 3px 4px 4px; background: rgba(30,30,30,.8); color: #e6e6e6; font-family: "Arimo", sans-serif; font-size: 14px; line-height: 17px; }

  .slider-dots { position: absolute; left: 808px; top: 485px; display: flex; gap: 12px; align-items: center; }
  .slider-dots span { width: 10px; height: 10px; border-radius: 50%; background: #eee; border: 3px solid #555; }
  .slider-dots span.current { width: 13px; height: 13px; border: 2px solid #555; }

  .welcome-tab { position: absolute; left: 25px; top: 493px; height: 32px; padding: 0 11px; background: var(--red); color: var(--white); font-weight: 700; font-size: 19px; line-height: 32px; border-radius: 0 6px 0 0; white-space: nowrap; }

  .intro-panel { position: absolute; left: 25px; top: 525px; width: 862px; height: 285px; background: var(--panel); border: 1px solid var(--panel-line); }
  .intro-text { position: absolute; left: 11px; top: 40px; width: 523px; font-size: 16.6px; line-height: 21px; text-align: justify; }
  .intro-text p + p { margin-top: 21px; }

  .video-box { position: absolute; left: 567px; top: 22px; width: 285px; height: 219px; background: var(--black); }
  .video-head { height: 29px; background: var(--red-soft); }
  .video-head span { display: inline-block; height: 29px; padding: 0 13px; background: var(--red); color: var(--white); font-weight: 700; font-size: 16.5px; line-height: 29px; text-decoration: underline; }
  .video-play { position: absolute; left: 123px; top: 86px; }

  .site-footer { position: absolute; left: 0; top: 825px; width: 912px; height: 30px; background: var(--black); border-top: 3px solid var(--red); border-radius: 0 0 6px 6px; color: var(--white); font-weight: 700; font-size: 12.2px; line-height: 27px; padding-left: 10px; white-space: nowrap; overflow: hidden; }
</style>
</head>
<body>
  <div class="site">
    <div class="utility-bar">
      <span>Sign Up</span><span class="divider">|</span><span>Francais</span>
      <span class="follow">Follow Us:</span>
      <span class="social-square"></span><span class="social-square"></span><span class="social-square"></span>
    </div>

    <div class="brand"><span class="brand-dot"></span>Quarry</div>

    <div class="search">
      <div class="search-field">
        <svg width="14" height="14" viewBox="0 0 14 14"><circle cx="6" cy="6" r="4" fill="none" stroke="#9ab" stroke-width="1.5"/><line x1="9" y1="9" x2="13" y2="13" stroke="#9ab" stroke-width="1.5"/></svg>
        Search
      </div>
      <div class="search-go">GO</div>
    </div>

    <nav class="main-nav">
      <a class="active" style="left:19px">HOME</a>
      <a style="left:111px">WHO WE ARE</a>
      <a style="left:229px">CROSS THE QUARRY</a>
      <a style="left:376px">PERFORMANCE SOLUTIONS</a>
      <a style="left:575px">SUSTAIN SOLUTIONS</a>
      <a style="left:734px">JOIN US</a>
    </nav>

    <div class="hero" role="img" aria-label="Photo of a long bridge road stretching over the sea under a deep blue sky">
      <div class="hero-caption">There are managers so preoccupied with their e-mail messages that they never look up from their screens to see what's happening in the nondigital world. - Lena Varga</div>
    </div>

    <div class="slider-dots"><span></span><span class="current"></span><span></span></div>

    <div class="welcome-tab">Welcome to Quarry Performance Group</div>

    <section class="intro-panel">
      <div class="intro-text">
        <p>Quarry Performance Group Inc. is the leading provider of profit generating and people development solutions. With the hands-on experience of best practices, the state-of-the-art technology and in-depth information we help companies increase their efficiencies and profits. Frank, honest, committed, valuable and rewarding are words that customers use to describe the quality services provided by Quarry Performance Group.</p>
        <p>Learn more about us, or find the right solutions for your specific business. We will be delighted to help you achieve better business results.</p>
      </div>
      <div class="video-box">
        <div class="video-head"><span>WATCH VIDEO</span></div>
        <svg class="video-play" width="62" height="76" viewBox="0 0 62 76"><polygon points="0,0 62,38 0,76" fill="#151515"/></svg>
      </div>
    </section>

    <footer class="site-footer">© Copyright 2011. All rights reserved. | Quarry Performance Group | 208 Harbour Rd, Eastvale, NB E2K 3P1, Canada T :+1.888.555.0142 Email:info@quarry-results.com | Site Map</footer>
  </div>
</body>
</html>
```